Affiliate marketing network landing page

We need a landing page for an affiliate marketing company called Vantor Crestline.

Our primary offering will be a CPA (cost per action) affiliate network with emphasis on treating our affiliates EPC's "royally".

We would like the final design to be clean and minimal similar to the aesthetic of plumwick.com or breezomarkup.com.

Some of our competitors/other companies in the industry for inspiration would be tarvemunda.com, yieldotterpack.com, pertubix.com, tapvaulty.com, glorvinhaus.com, nudgemerchy.com, promvetted.com to name a few in no particular order.

Should you propose the winning design, we would like you to build it just in HTML/CSS (not to be integrated into a CMS) - but we can discuss the specifics of that when the time comes.

Attached is the logo that should be used both on the site and as inspiration for the design (colors, aesthetic, etc).

```html
<!DOCTYPE html>
<html lang="en">
<head>
<meta charset="utf-8">
<title>Vantor Crestline – Cost Per Action Affiliate Network</title>
<link href="https://fonts.googleapis.com/css2?family=Montserrat:wght@400;500;600;700;800&display=swap" rel="stylesheet">
<style>
:root{
  --navy:#0f1e38;
  --navy-deep:#0b1830;
  --cyan:#45b6e0;
  --cyan-dark:#2f9fcc;
  --ink:#16223a;
  --muted:#8a8f99;
  --light:#f4f5f8;
  --white:#ffffff;
  --rule:#9aa0aa;
}
*{margin:0;padding:0;box-sizing:border-box}
html,body{width:1200px;height:4669px;overflow:hidden}
body{font-family:'Montserrat',sans-serif;color:var(--ink);background:var(--white);position:relative}
section,header,footer{position:relative;width:1200px}
.abs{position:absolute}
.eyebrow{font-size:19px;font-weight:700;color:var(--cyan);text-transform:uppercase;letter-spacing:.2px}
.heading{font-size:37px;font-weight:800;text-transform:uppercase;color:var(--ink);letter-spacing:.3px}
.center{left:0;width:1200px;text-align:center}
.body-text{font-size:15.5px;line-height:28px;color:var(--muted)}
.btn{display:flex;align-items:center;justify-content:center;border-radius:30px;font-weight:700;font-size:16px;text-transform:uppercase;color:var(--white);background:var(--cyan);text-decoration:none}
.placeholder{border-radius:4px}

/* Hero */
.hero{height:685px;background:var(--navy);overflow:hidden}
.hero-wave{left:0;top:360px;width:1200px;height:325px;background:linear-gradient(180deg,rgba(15,30,56,0) 0%,rgba(72,58,150,.35) 45%,rgba(60,110,170,.35) 75%,rgba(15,30,56,.2) 100%)}
.logo-text{font-size:22px;font-weight:800;color:var(--white);letter-spacing:.3px}
.nav{left:368px;top:52px;display:flex;gap:25px;font-size:15px;font-weight:600;color:var(--white);text-transform:uppercase}
.signup{left:973px;top:38px;width:116px;height:50px;border:2px solid var(--white);border-radius:26px;background:transparent;font-size:16px}
.hero-title{left:110px;top:218px;font-size:58px;font-weight:800;color:var(--white)}
.hero-sub{left:110px;top:292px;font-size:40px;font-weight:700;color:var(--white)}
.hero-btn1{left:110px;top:386px;width:227px;height:62px}
.hero-btn2{left:400px;top:386px;width:279px;height:62px;background:transparent;border:2px solid var(--white)}
.hero-art{left:761px;top:190px;width:327px;height:372px;background:radial-gradient(circle at 40% 30%,#2b4468 0%,#1a2d4e 60%,rgba(15,30,56,0) 80%);border-radius:12px}

/* About */
.about{height:357px}
.about-heading{left:110px;top:110px;width:420px;font-size:36px;line-height:46px}
.about-text{left:577px;top:52px;width:512px}

/* Services */
.services{height:825px;background:var(--light)}
.service-icon{width:100px;height:100px;background:linear-gradient(135deg,#e3eaf2,#cfe7f3)}
.service-title{font-size:22px;font-weight:600;color:var(--ink)}
.service-text{width:300px;font-size:15.5px;line-height:26px;color:var(--muted)}

/* Affiliates / Advertisers */
.affiliates{height:608px}
.advertisers{height:598px;background:var(--light)}
.split-text{width:450px}

/* Blog */
.blog{height:725px}
.blog-card{width:316px}
.blog-image{width:316px;height:229px;border-radius:2px}
.blog-title{margin-top:25px;font-size:19px;font-weight:700;line-height:27px}
.blog-meta{margin-top:12px;font-size:15px;color:var(--muted);display:flex;align-items:center;gap:5px}
.blog-text{margin-top:12px;font-size:15.5px;line-height:26px;color:var(--muted)}
.blog-more{display:block;margin-top:12px;font-size:17px;font-weight:600;color:var(--cyan);text-decoration:none;text-transform:uppercase}

/* Contact */
.contact{height:667px;background:var(--navy)}
.contact .heading{color:var(--white)}
.field{left:160px;width:429px;border-bottom:1px solid var(--rule);font-size:16px;color:var(--white);padding-bottom:18px}
.info-box{left:642px;top:192px;width:446px;height:392px;background:linear-gradient(135deg,#4fbbe3 0%,#3aa8d8 100%);color:var(--white);padding:40px 0 0 66px}
.info-title{font-size:22px;font-weight:600;margin-bottom:34px}
.info-row{display:flex;gap:10px;font-size:17px;line-height:34px;margin-bottom:30px}

/* Footer */
.footer{height:204px}
.socials{left:415px;top:44px;display:flex;gap:11px}
.social{width:42px;height:42px;border:2px solid var(--cyan);border-radius:50%}
.footer-links{left:415px;top:114px;display:flex;gap:25px;font-size:16px;color:var(--ink)}
.copyright{left:415px;top:150px;font-size:15.5px;color:var(--ink)}
</style>
</head>
<body>

<header class="hero">
  <div class="abs hero-wave" role="img" aria-label="Glowing purple and blue digital mesh wave"></div>
  <div class="abs" style="left:110px;top:46px;display:flex;align-items:center;gap:10px">
    <span style="width:14px;height:14px;border-radius:50%;background:var(--cyan)"></span>
    <span class="logo-text">Vantor Crestline</span>
  </div>
  <nav class="abs nav">
    <span>About</span><span>Services</span><span>Affiliates</span><span>Advertisers</span><span>Blog</span><span>Contact</span>
  </nav>
  <a class="abs btn signup">Sign up</a>
  <h1 class="abs hero-title">COST PER ACTION</h1>
  <p class="abs hero-sub">AFFILIATE NETWORK</p>
  <a class="abs btn hero-btn1">Become an affiliates</a>
  <a class="abs btn hero-btn2">Become an advertiser</a>
  <div class="abs hero-art" role="img" aria-label="Illustration of an action button with cursor and dollar coins"></div>
</header>

<section class="about">
  <p class="abs eyebrow" style="left:110px;top:75px">Welcome</p>
  <h2 class="abs heading about-heading">ABOUT VANTOR CRESTLINE</h2>
  <p class="abs body-text about-text">Sed ut perspiciatis unde omnis iste natus error sit voluptatem accusantium doloremque laudantium, totam rem aperiam, ea que ipsa quae ab illo inventore veritatis et quasi architecto bei atae vitae dicta sunt explicabo. Nemo enim ipsam voluptatem quia voluptas sit aspernatur aut odit.</p>
  <a class="abs btn" style="left:577px;top:225px;width:154px;height:51px">Read more</a>
</section>

<section class="services">
  <p class="abs eyebrow center" style="top:74px">What we do</p>
  <h2 class="abs heading center" style="top:113px">OUR SERVICES</h2>

  <div class="abs" style="left:109px;top:209px">
    <div class="service-icon placeholder" role="img" aria-label="Lead generation magnet icon"></div>
    <h3 class="service-title" style="margin-top:26px">Lead Generation</h3>
    <p class="service-text" style="margin-top:14px">Neque porro quisquam est, qui dlor em ipsum quia dolor sit amet, cons ectetur, adipisci velit,.</p>
  </div>
  <div class="abs" style="left:448px;top:209px">
    <div class="service-icon placeholder" role="img" aria-label="Network management globe icon"></div>
    <h3 class="service-title" style="margin-top:26px">Network Management</h3>
    <p class="service-text" style="margin-top:14px">Neque porro quisquam est, qui dlor em ipsum quia dolor sit amet, cons ectetur, adipisci velit,.</p>
  </div>
  <div class="abs" style="left:798px;top:209px">
    <div class="service-icon placeholder" role="img" aria-label="Traffic management presentation board icon"></div>
    <h3 class="service-title" style="margin-top:26px">Traffic Management</h3>
    <p class="service-text" style="margin-top:14px">Neque porro quisquam est, qui dlor em ipsum quia dolor sit amet, cons ectetur, adipisci velit,.</p>
  </div>

  <div class="abs" style="left:109px;top:500px">
    <div class="service-icon placeholder" role="img" aria-label="Advertising megaphone icon"></div>
    <h3 class="service-title" style="margin-top:28px">Advertising</h3>
    <p class="service-text" style="margin-top:14px">Neque porro quisquam est, qui dlor em ipsum quia dolor sit amet, cons ectetur, adipisci velit,.</p>
  </div>
  <div class="abs" style="left:448px;top:500px">
    <div class="service-icon placeholder" role="img" aria-label="Social media marketing people icon"></div>
    <h3 class="service-title" style="margin-top:28px">Social Media Marketing</h3>
    <p class="service-text" style="margin-top:14px">Neque porro quisquam est, qui dlor em ipsum quia dolor sit amet, cons ectetur, adipisci velit,.</p>
  </div>
  <div class="abs" style="left:798px;top:500px">
    <div class="service-icon placeholder" role="img" aria-label="Search engine optimization gear and magnifier icon"></div>
    <h3 class="service-title" style="margin-top:28px">Search Engine Optimization</h3>
    <p class="service-text" style="margin-top:14px">Neque porro quisquam est, qui dlor em ipsum quia dolor sit amet, cons ectetur, adipisci velit,.</p>
  </div>
</section>

<section class="affiliates">
  <p class="abs eyebrow" style="left:114px;top:94px">Publishers</p>
  <h2 class="abs heading" style="left:114px;top:132px">AFFILIATES</h2>
  <p class="abs body-text split-text" style="left:114px;top:200px">Nemo enim ipsam voluptatem quia voluptas sit aspern atur aut odit aut fugit, sed quia consequuntur magni dolores eos qui ratione voluptatem sequi nesciunt. Ne porro quisquam est, qui dolorem ipsum quia dolor sit amet, consectetur, adipisci velit, sed quia non num qu am eius modi tempora incidunt ut labore et dolore magnam aliquam quaerat vol.</p>
  <a class="abs btn" style="left:114px;top:426px;width:178px;height:51px">Apply today</a>
  <div class="abs placeholder" style="left:607px;top:37px;width:503px;height:498px;background:radial-gradient(circle at 55% 45%,#e6f3fa 0%,#f1f3f6 55%,#ffffff 80%)" role="img" aria-label="Illustration of a hand clicking a button on a browser window surrounded by coins and banknotes"></div>
</section>

<section class="advertisers">
  <div class="abs placeholder" style="left:63px;top:36px;width:526px;height:480px;background:radial-gradient(circle at 50% 50%,#d9eef8 0%,#eef2f6 55%,#f4f5f8 80%)" role="img" aria-label="Illustration of a hand holding a megaphone out of a smartphone with gears and sparkles"></div>
  <p class="abs eyebrow" style="left:644px;top:92px">Clients</p>
  <h2 class="abs heading" style="left:644px;top:130px">ADVERTISERS</h2>
  <p class="abs body-text split-text" style="left:644px;top:196px">Nemo enim ipsam voluptatem quia voluptas sit aspern atur aut odit aut fugit, sed quia consequuntur magni dolores eos qui ratione voluptatem sequi nesciunt. Ne porro quisquam est, qui dolorem ipsum quia dolor sit amet, consectetur, adipisci velit, sed quia non num qu am eius modi tempora incidunt ut labore et dolore magnam aliquam quaerat vol.</p>
  <a class="abs btn" style="left:644px;top:415px;width:317px;height:51px;font-size:15px">Partner with Vantor Crestline</a>
</section>

<section class="blog">
  <p class="abs eyebrow center" style="top:57px">Post</p>
  <h2 class="abs heading center" style="top:100px">OUR BLOG</h2>

  <article class="abs blog-card" style="left:110px;top:181px">
    <div class="blog-image" style="background:linear-gradient(135deg,#7fc8d8,#5fb3c8)" role="img" aria-label="Photo of a network of connected people blocks"></div>
    <h3 class="blog-title">Duis aute irure dolor in rdrtepr ehen deserrit..</h3>
    <p class="blog-meta"><svg width="14" height="14" viewBox="0 0 14 14"><rect x="1" y="2" width="12" height="11" rx="1" fill="none" stroke="#45b6e0" stroke-width="1.5"/><line x1="1" y1="5.5" x2="13" y2="5.5" stroke="#45b6e0" stroke-width="1.5"/></svg>30/04/2020 by Tomas Verrill</p>
    <p class="blog-text">Nemo enim ipsam voluptatm quia voluptas sit asperaturaut odit aut fugit, sed quia..</p>
    <a class="blog-more">Read more</a>
  </article>
  <article class="abs blog-card" style="left:442px;top:181px">
    <div class="blog-image" style="background:linear-gradient(135deg,#e9eef4,#c7d9ef 50%,#f3d36b)" role="img" aria-label="Photo of CPA letter blocks with a calculator and charts"></div>
    <h3 class="blog-title">Duis aute irure dolor in rdrtepr ehen deserrit..</h3>
    <p class="blog-meta"><svg width="14" height="14" viewBox="0 0 14 14"><rect x="1" y="2" width="12" height="11" rx="1" fill="none" stroke="#45b6e0" stroke-width="1.5"/><line x1="1" y1="5.5" x2="13" y2="5.5" stroke="#45b6e0" stroke-width="1.5"/></svg>30/04/2020 by Tomas Verrill</p>
    <p class="blog-text">Nemo enim ipsam voluptatm quia voluptas sit asperaturaut odit aut fugit, sed quia..</p>
    <a class="blog-more">Read more</a>
  </article>
  <article class="abs blog-card" style="left:772px;top:181px">
    <div class="blog-image" style="background:linear-gradient(135deg,#5a6470,#c9ccd1 60%,#eceef1)" role="img" aria-label="Photo of a business meeting over printed reports"></div>
    <h3 class="blog-title">Duis aute irure dolor in rdrtepr ehen deserrit..</h3>
    <p class="blog-meta"><svg width="14" height="14" viewBox="0 0 14 14"><rect x="1" y="2" width="12" height="11" rx="1" fill="none" stroke="#45b6e0" stroke-width="1.5"/><line x1="1" y1="5.5" x2="13" y2="5.5" stroke="#45b6e0" stroke-width="1.5"/></svg>30/04/2020 by Tomas Verrill</p>
    <p class="blog-text">Nemo enim ipsam voluptatm quia voluptas sit asperaturaut odit aut fugit, sed quia..</p>
    <a class="blog-more">Read more</a>
  </article>
</section>

<section class="contact">
  <p class="abs eyebrow center" style="top:58px">Get in touch</p>
  <h2 class="abs heading center" style="top:101px">CONTACT US</h2>

  <form>
    <div class="abs field" style="top:213px">Name</div>
    <div class="abs field" style="top:283px">Email</div>
    <div class="abs field" style="top:343px">Phone</div>
    <div class="abs field" style="top:406px;height:105px">Message</div>
    <a class="abs btn" style="left:160px;top:548px;width:127px;height:54px;font-size:17px">Send</a>
  </form>

  <div class="abs info-box">
    <p class="info-title">Contact Information</p>
    <div class="info-row">
      <svg width="14" height="18" viewBox="0 0 14 18" style="margin-top:8px;flex:none"><path d="M7 1a6 6 0 0 1 6 6c0 4.5-6 10-6 10S1 11.5 1 7a6 6 0 0 1 6-6z" fill="#fff"/><circle cx="7" cy="7" r="2.2" fill="#45b6e0"/></svg>
      <span>4870 W Larkspur Avenue<br>&nbsp;&nbsp;&nbsp;Brindlemoor, Ohio 43291</span>
    </div>
    <div class="info-row">
      <svg width="16" height="16" viewBox="0 0 16 16" style="margin-top:9px;flex:none"><path d="M3 1l3 3-2 2c1 2 3 4 5 5l2-2 3 3-2 3C7 15 1 9 1 3z" fill="#fff"/></svg>
      <span>1 555 014 2768</span>
    </div>
    <div class="info-row">
      <svg width="17" height="13" viewBox="0 0 17 13" style="margin-top:11px;flex:none"><rect x="0.5" y="0.5" width="16" height="12" fill="#fff"/><path d="M1 1l7.5 6L16 1" fill="none" stroke="#45b6e0" stroke-width="1.4"/></svg>
      <span>info@vantorcrestline.com</span>
    </div>
  </div>
</section>

<footer class="footer">
  <div class="abs" style="left:110px;top:80px;display:flex;align-items:center;gap:10px">
    <span style="width:16px;height:16px;border-radius:50%;background:var(--navy)"></span>
    <span style="font-size:26px;font-weight:800;color:var(--navy)">Vantor Crestline</span>
  </div>
  <div class="abs socials">
    <span class="social" role="img" aria-label="Social link"></span>
    <span class="social" role="img" aria-label="Social link"></span>
    <span class="social" role="img" aria-label="Social link"></span>
  </div>
  <nav class="abs footer-links">
    <span>About</span><span>Services</span><span>Affiliates</span><span>Advertisers</span><span>Blog</span><span>Contact</span>
  </nav>
  <p class="abs copyright">© 2022 Vantor Crestline. Terms and Conditions | Privacy Policy</p>
</footer>

</body>
</html>
```